Brochure Design for agricultural helicopter company

Redgum Aerial is an agricultural helicopter company based in Victoria, Australia.<br/>We require an updated tri fold brochure design to advertise our services.<br/>I will attach our current brochure design in the files, we would prefer as many images of our new grey helicopter as possible.<br/>We were pretty happy with the text and general design of the existing brochure however we just want a more up to date version.<br/>some prices we would like included but not to stand out too much are for Spraying from $36 per hectare and Fertiliser Spreading from $280 per tonne<br/>Our target audience is mainly farmers.<br/>Please feel free to visit our website and facebook page to learn more about our services www.redgumaerial.com.au<br/>Thanks

```html
<!DOCTYPE html>
<html lang="en">
<head>
<meta charset="utf-8">
<title>Redgum Aerial – Tri-fold Brochure</title>
<link rel="stylesheet" href="https://fonts.googleapis.com/css2?family=Open+Sans:wght@400;600;700&family=Oswald:wght@500;600;700&display=swap">
<style>
  :root{
    --canvas:#e3e3e3;
    --blue:#1b609c;
    --blue-deep:#154a7c;
    --green:#6cb33f;
    --green-light:#8cc63f;
    --sky:#8fb8dc;
    --paddock:#6f8f45;
    --ink:#3a3a3a;
    --white:#ffffff;
  }
  *{box-sizing:border-box;margin:0;padding:0}
  html,body{width:1200px;height:2400px;overflow:hidden}
  body{background:var(--canvas);font-family:"Open Sans",Arial,sans-serif;color:var(--ink);position:relative}
  .spread{position:absolute;left:30px;width:1140px;height:800px;display:flex;box-shadow:0 8px 24px rgba(0,0,0,.18)}
  .spread--outside{top:300px}
  .spread--inside{top:1260px}
  .panel{position:relative;width:380px;height:800px;overflow:hidden;background:var(--white)}
  .panel svg.bg{position:absolute;inset:0;width:380px;height:800px}
  .abs{position:absolute}
  .brand{display:flex;align-items:center;gap:10px;font-family:"Open Sans",Arial,sans-serif;font-weight:700;font-size:30px;color:var(--blue);white-space:nowrap}
  .brand-dot{width:26px;height:26px;border-radius:50%;background:var(--green)}
  .brand--light{color:var(--white)}
  .brand--light .brand-dot{background:var(--white)}
  .headline{font-family:"Oswald",Arial Narrow,sans-serif;font-weight:700;color:var(--white);text-transform:uppercase;line-height:1.05}
  .section-title{font-family:"Oswald",Arial Narrow,sans-serif;font-weight:600;font-size:19px;text-transform:uppercase;letter-spacing:.5px;color:var(--blue);border-bottom:1px solid var(--blue);padding-bottom:3px;margin-bottom:8px;display:inline-block}
  .section-title--green{color:var(--green);border-color:var(--green)}
  .section-title--light{color:var(--white);border-color:var(--white)}
  .body-copy{font-size:11.5px;line-height:1.6}
  .body-copy--light{color:var(--white)}
  .price{font-family:"Oswald",Arial Narrow,sans-serif;font-weight:600;font-size:13px;color:var(--green);text-transform:uppercase;letter-spacing:.3px}
  .web-band{font-family:"Open Sans",Arial,sans-serif;font-weight:700;color:var(--white);font-size:19px}
  .phone-line{display:flex;align-items:center;gap:10px;font-family:"Oswald",Arial Narrow,sans-serif;font-weight:600;color:var(--white);font-size:22px;letter-spacing:1px}
  .service-list{list-style:none}
  .service-list li{display:flex;align-items:center;gap:12px;font-family:"Oswald",Arial Narrow,sans-serif;font-weight:500;font-size:14px;color:var(--blue);text-transform:uppercase;padding:6px 0;border-bottom:1px solid #d7e3ef}
  .service-icon{width:18px;height:18px;border-radius:50%;background:var(--blue);flex:none}
  .social{display:flex;gap:10px}
  .social span{width:22px;height:22px;border:1.5px solid var(--white);border-radius:50%}
  .photo-circle{border-radius:50%;border:6px solid var(--white);box-shadow:0 2px 6px rgba(0,0,0,.25)}
  .caption{font-size:10px;font-style:italic;line-height:1.5;color:#555}
</style>
</head>
<body>

<!-- OUTSIDE SPREAD -->
<section class="spread spread--outside">

  <!-- Services flap -->
  <article class="panel panel--services">
    <svg class="bg" viewBox="0 0 380 800" aria-hidden="true">
      <path d="M0,520 Q200,470 380,545 L380,800 L0,800 Z" fill="var(--blue)"/>
      <path d="M0,540 Q200,490 380,565 L380,800 L0,800 Z" fill="var(--white)"/>
    </svg>
    <div class="abs" style="left:0;top:548px;width:380px;height:252px;clip-path:path('M0,0 Q200,-50 380,25 L380,252 L0,252 Z');background:linear-gradient(180deg,#a9c8e4 0%,#cfe0ee 45%,#7c9a4e 62%,#5d7a38 100%)" role="img" aria-label="Grey helicopter spraying a paddock with booms extended"></div>
    <div class="abs" style="left:34px;top:48px;width:312px">
      <h2 class="section-title">Our Services</h2>
      <ul class="service-list">
        <li><span class="service-icon"></span>Helicopter Spraying</li>
        <li><span class="service-icon"></span>Helicopter Seeding</li>
        <li><span class="service-icon"></span>Fertiliser Spreading / Topdressing</li>
        <li><span class="service-icon"></span>Fine Particle Fertiliser Application</li>
        <li><span class="service-icon"></span>Helicopter Crop Protection</li>
        <li><span class="service-icon"></span>Commercial Helicopter Work</li>
        <li><span class="service-icon"></span>Feral Animal Control</li>
        <li><span class="service-icon"></span>Helicopter Charters</li>
      </ul>
      <p class="price" style="margin-top:18px">Spraying from $36 per hectare</p>
      <p class="price">Fertiliser spreading from $280 per tonne</p>
    </div>
  </article>

  <!-- Contact back panel -->
  <article class="panel panel--contact">
    <svg class="bg" viewBox="0 0 380 800" aria-hidden="true">
      <rect width="380" height="800" fill="var(--green-light)"/>
      <path d="M0,480 Q190,420 380,470 L380,800 L0,800 Z" fill="var(--blue)"/>
      <rect y="730" width="380" height="70" fill="var(--green)"/>
    </svg>
    <div class="abs brand brand--light" style="left:70px;top:70px"><span class="brand-dot"></span>Redgum Aerial</div>
    <div class="abs" style="left:0;top:170px;width:380px;text-align:center;color:var(--white)">
      <h2 class="section-title section-title--light">Contact Us</h2>
      <p style="font-family:'Oswald',sans-serif;font-weight:500;font-size:16px;text-transform:uppercase;margin-top:6px">Agricultural Helicopter Services</p>
      <p class="body-copy">High Country | Gippsland | Murray</p>
      <p class="body-copy" style="margin-top:12px">admin@redgumaerial.com.au</p>
      <p class="body-copy">www.redgumaerial.com.au</p>
    </div>
    <div class="abs photo-circle" style="left:130px;top:395px;width:120px;height:120px;background:linear-gradient(180deg,#b9d3ea 0%,#d8e6c0 50%,#7e9a4c 100%)" role="img" aria-label="Helicopter parked on a grassy airstrip"></div>
    <div class="abs body-copy body-copy--light" style="left:0;top:560px;width:380px;text-align:center">
      <p>Redgum Aerial Pty Ltd</p>
      <p>Daniel Hartley</p>
      <p>0400 555 019</p>
    </div>
    <div class="abs social" style="left:156px;top:645px" aria-label="Social media"><span></span><span></span><span></span></div>
    <div class="abs phone-line" style="left:0;top:748px;width:380px;justify-content:center">
      <svg width="20" height="20" viewBox="0 0 24 24" aria-hidden="true"><path fill="var(--white)" d="M6.6 10.8a15.1 15.1 0 0 0 6.6 6.6l2.2-2.2a1 1 0 0 1 1-.25 11.4 11.4 0 0 0 3.6.57 1 1 0 0 1 1 1V20a1 1 0 0 1-1 1A17 17 0 0 1 3 4a1 1 0 0 1 1-1h3.5a1 1 0 0 1 1 1c0 1.25.2 2.45.57 3.57a1 1 0 0 1-.25 1z"/></svg>
      0400 555 019
    </div>
  </article>

  <!-- Cover -->
  <article class="panel panel--cover">
    <svg class="bg" viewBox="0 0 380 800" aria-hidden="true">
      <path d="M0,470 Q200,560 380,480 L380,800 L0,800 Z" fill="var(--blue)"/>
      <path d="M0,175 Q190,120 380,160 L380,190 Q190,150 0,205 Z" fill="var(--green)"/>
      <rect y="725" width="380" height="75" fill="var(--green)"/>
    </svg>
    <div class="abs" style="left:0;top:200px;width:380px;height:340px;clip-path:path('M0,5 Q190,-50 380,-10 L380,275 Q200,355 0,265 Z');background:linear-gradient(180deg,#7fb0dd 0%,#a8c9e6 30%,#7d9a52 55%,#5c7b37 100%)" role="img" aria-label="Grey helicopter spraying over green hill country"></div>
    <div class="abs brand" style="left:90px;top:70px"><span class="brand-dot"></span>Redgum Aerial</div>
    <h1 class="abs headline" style="left:0;top:588px;width:380px;text-align:center;font-size:40px">Agricultural<br>Helicopter Services</h1>
    <p class="abs web-band" style="left:0;top:748px;width:380px;text-align:center">www.redgumaerial.com.au</p>
  </article>
</section>

<!-- INSIDE SPREAD -->
<section class="spread spread--inside">

  <!-- About -->
  <article class="panel panel--about">
    <svg class="bg" viewBox="0 0 380 800" aria-hidden="true">
      <rect width="380" height="800" fill="var(--blue)"/>
      <path d="M0,555 Q190,510 380,540 L380,800 L0,800 Z" fill="var(--white)"/>
    </svg>
    <div class="abs" style="left:0;top:565px;width:380px;height:235px;clip-path:path('M0,0 Q190,-45 380,-15 L380,235 L0,235 Z');background:linear-gradient(180deg,#9fc1e2 0%,#c8dcee 45%,#76984a 60%,#4f6f2f 100%)" role="img" aria-label="Helicopter lifting off beside a ground support truck"></div>
    <div class="abs" style="left:30px;top:40px;width:320px">
      <h2 class="section-title section-title--green">About Us</h2>
      <p class="body-copy body-copy--light">Redgum Aerial was founded with a view to helping farm and forestry clients obtain maximum production and profitability from their land through the targeted application of specialised chemicals and fertilisers. With all of our staff members having grown up in agriculture, we understand the importance of timing and accuracy for every job we take on.</p>
      <p class="body-copy body-copy--light" style="margin-top:12px">Our helicopter is equipped with low-drift spray booms and GPS guidance for accuracy. We service the High Country, Gippsland and the Murray, and can travel anywhere in between.</p>
    </div>
    <div class="abs photo-circle" style="left:28px;top:445px;width:120px;height:120px;background:radial-gradient(circle,#3b2a22 0%,#5a4033 60%,#6f5240 100%)" role="img" aria-label="Close view of fine fertiliser granules"></div>
  </article>

  <!-- Services detail -->
  <article class="panel panel--detail">
    <svg class="bg" viewBox="0 0 380 800" aria-hidden="true">
      <rect y="730" width="380" height="70" fill="var(--green)"/>
    </svg>
    <div class="abs" style="left:30px;top:34px;width:320px">
      <h2 class="section-title">Spraying</h2>
      <p class="body-copy">Aerial spraying is a quick, accurate and cost effective means of weed control on your farm. Compared to a ground rig, a helicopter causes no soil compaction and reaches steep country with ease.</p>
      <p class="price" style="margin-top:4px">Spraying from $36 per hectare</p>
      <h2 class="section-title" style="margin-top:16px">Fertiliser Application</h2>
      <p class="body-copy">Fertiliser application by helicopter is cost effective and fast. We can apply most products including urea, super and lime, and our loading crew keeps the machine turning around quickly.</p>
      <p class="price" style="margin-top:4px">Fertiliser spreading from $280 per tonne</p>
    </div>
    <div class="abs" style="left:40px;top:405px;width:300px;height:130px;border:4px solid var(--white);box-shadow:0 2px 6px rgba(0,0,0,.25);background:linear-gradient(180deg,#a7c6e3 0%,#c6d9ea 35%,#7f9d52 55%,#5a7a35 100%)" role="img" aria-label="Helicopter spreading fertiliser over a paddock"></div>
    <p class="abs caption" style="left:40px;top:545px;width:300px">All of our equipment is calibrated to ensure an accurate and even spread of your product.</p>
    <div class="abs" style="left:30px;top:590px;width:320px">
      <h2 class="section-title">Seeding</h2>
      <p class="body-copy">Aerial seeding or over-sowing is a great way of improving pasture on hills and paddocks that are otherwise hard to reach. Seed is spread evenly and quickly for a strong, productive result.</p>
    </div>
    <div class="abs phone-line" style="left:0;top:748px;width:380px;justify-content:center">
      <svg width="20" height="20" viewBox="0 0 24 24" aria-hidden="true"><path fill="var(--white)" d="M6.6 10.8a15.1 15.1 0 0 0 6.6 6.6l2.2-2.2a1 1 0 0 1 1-.25 11.4 11.4 0 0 0 3.6.57 1 1 0 0 1 1 1V20a1 1 0 0 1-1 1A17 17 0 0 1 3 4a1 1 0 0 1 1-1h3.5a1 1 0 0 1 1 1c0 1.25.2 2.45.57 3.57a1 1 0 0 1-.25 1z"/></svg>
      0400 555 019
    </div>
  </article>

  <!-- Fine particle -->
  <article class="panel panel--fine">
    <svg class="bg" viewBox="0 0 380 800" aria-hidden="true">
      <rect width="380" height="800" fill="var(--blue)"/>
      <path d="M0,0 L380,0 L380,215 Q190,290 0,240 Z" fill="var(--white)"/>
      <rect y="730" width="380" height="70" fill="var(--green)"/>
    </svg>
    <div class="abs" style="left:0;top:0;width:380px;height:240px;clip-path:path('M0,0 L380,0 L380,205 Q190,280 0,230 Z');background:linear-gradient(180deg,#6c8d6a 0%,#8aa7a0 35%,#b77a3a 60%,#c98a3d 100%)" role="img" aria-label="Helicopter landed beside a farm dam in autumn grass"></div>
    <div class="abs" style="left:30px;top:285px;width:320px">
      <h2 class="headline" style="color:var(--green-light);font-size:24px;font-weight:600">Fine Particle Fertiliser<br>Supply and Application</h2>
      <p class="body-copy body-copy--light" style="margin-top:14px">Redgum Aerial is pleased to offer an exciting new service: fine particle fertiliser applied by helicopter. Finely ground products are taken up quickly by pasture and crops, giving faster results from smaller rates.</p>
      <h3 class="section-title section-title--green" style="margin-top:16px;font-size:15px">How It Works</h3>
      <p class="body-copy body-copy--light">Our specialised spreading bucket meters the fine product evenly across every paddock, so each hectare receives exactly the rate it needs with little waste.</p>
    </div>
    <p class="abs web-band" style="left:0;top:748px;width:380px;text-align:center">www.redgumaerial.com.au</p>
  </article>
</section>

</body>
</html>
```